Design for a Service-Based Estimate

We want a design for an Estimate that will always be sent in PDF format. The estimate or proposal is a critical document that needs to plainly show the service items, item description but also needs to be attractive and professional looking. Our current estimate deliverable is attached but it looks really basic like a Word document

```html
<!DOCTYPE html>
<html lang="en">
<head>
<meta charset="utf-8">
<title>Firm Grade – Terms and Conditions</title>
<link rel="stylesheet" href="https://fonts.googleapis.com/css2?family=Source+Sans+3:ital,wght@0,400;0,700;1,400&family=Sacramento&display=swap">
<style>
  :root {
    --brand-red: #cf4a32;
    --brand-navy: #2e2c4b;
    --band-navy: #35304f;
    --text-grey: #4f4f55;
    --rule-grey: #9a9aa0;
    --faint-grey: #e6e6e9;
    --paper: #ffffff;
  }
  * { margin: 0; padding: 0; box-sizing: border-box; }
  html, body { width: 848px; height: 1200px; overflow: hidden; background: var(--paper); }
  .page {
    position: relative;
    width: 848px;
    height: 1200px;
    font-family: "Source Sans 3", Arial, sans-serif;
    color: var(--text-grey);
  }
  .side-bar {
    position: absolute; left: 47px; top: 0;
    width: 37px; height: 654px;
    background: var(--brand-red);
  }
  .brand-name {
    position: absolute; left: 0; right: 0; top: 44px;
    text-align: center;
    font-size: 50px; font-weight: 700; letter-spacing: 4px;
    color: var(--brand-navy);
    line-height: 60px;
  }
  .header-rule {
    position: absolute; left: 84px; top: 148px;
    width: 718px; height: 1px; background: var(--rule-grey);
  }
  .terms-title {
    position: absolute; left: 0; right: 0; top: 176px;
    text-align: center;
    font-size: 21px; font-weight: 400;
    color: var(--brand-navy);
  }
  .term {
    position: absolute; left: 94px; width: 720px;
    font-size: 13.4px; line-height: 17px;
  }
  .term-marker {
    position: absolute; left: -47px; top: 8px;
    width: 33px; height: 1.5px; background: var(--paper);
  }
  .signature-script {
    position: absolute; left: 44px; top: 672px;
    font-family: "Sacramento", cursive;
    font-size: 74px; line-height: 90px;
    color: var(--text-grey);
  }
  .signature-rule {
    position: absolute; left: 85px; top: 777px;
    width: 197px; height: 1px; background: var(--rule-grey);
  }
  .signature-label {
    position: absolute; left: 107px; top: 783px;
    font-size: 18px; font-style: italic;
    color: var(--text-grey);
  }
  .corner-bar {
    position: absolute; left: 805px; top: 1002px;
    width: 36px; height: 159px;
    background: var(--brand-red);
  }
  .brand-faint {
    position: absolute; left: 0; right: 0; top: 1054px;
    text-align: center;
    font-size: 74px; font-weight: 700; letter-spacing: 6px;
    line-height: 74px;
    color: var(--faint-grey);
  }
  .footer-rule {
    position: absolute; left: 47px; top: 1144px;
    width: 755px; height: 1px; background: var(--brand-navy);
  }
  .footer-band {
    position: absolute; left: 0; top: 1161px;
    width: 848px; height: 39px;
    background: var(--band-navy);
  }
</style>
</head>
<body>
<main class="page">
  <div class="side-bar"></div>

  <header>
    <div class="brand-name">FIRM GRADE</div>
    <div class="header-rule"></div>
  </header>

  <h1 class="terms-title">Terms and Conditions</h1>

  <section class="terms">
    <p class="term" style="top:227px"><span class="term-marker"></span>Prices as quoted in this estimate are valid for (60) days only.</p>
    <p class="term" style="top:260px"><span class="term-marker"></span>Payment in full, less any previously paid amounts, is due to the Contractor upon completion of the proposed scope of work.</p>
    <p class="term" style="top:314px"><span class="term-marker"></span>All change order requests must be communicated in writting to the Contractor by the Client or their authorized representative.</p>
    <p class="term" style="top:364px"><span class="term-marker"></span>All measurements listed in this estimate are approximate and may vary slightly due to actual field conditions.</p>
    <p class="term" style="top:398px"><span class="term-marker"></span>It is agreed by the Contractor and the Client that complications and costs arising from unforeseen conditions and handling of unsuitable materials are not included in this estimate.</p>
    <p class="term" style="top:451px"><span class="term-marker"></span>Unless specifically listed in this estimate, the following items and their costs are not included:<br>Maintenance of Traffic, Concrete Material Pumping, Testing, Excavation, Grading and Fill Material, Permits and Fees, Surveying and As-builts, Irrigation Repair, Landscaping and Root Mitigation, De-watering, Private Locates and Accessibility.</p>
    <p class="term" style="top:536px">Private utility locating services using radio detection devices and, when necessary, ground penetrating radar are offered by Firm Grade to assist in finding private utilities that may not have been located by the public one call system. Firm Grade will not be responsible for private utilities that have not been located nor for the failure of the above equipment to accurately detect existing utilities since the equipment is fallible and existing site conditions may preclude the ability of the equipment to detect an identifiable signal.</p>
  </section>

  <section class="signature">
    <div class="signature-script">Client Signature</div>
    <div class="signature-rule"></div>
    <div class="signature-label">Client Signature</div>
  </section>

  <footer>
    <div class="corner-bar"></div>
    <div class="brand-faint" aria-hidden="true">FIRM GRADE</div>
    <div class="footer-rule"></div>
    <div class="footer-band"></div>
  </footer>
</main>
</body>
</html>
```